PACKAGING AND LABEL DESIGN FOR LUXURY WHISKY BRAND

We need a label and packaging design for a new luxury whisky brand based in Singapore called Morvane. We need a label design and a suggested packaging design in a box/bag or wrap form. For the bottle it is fixed, so we would like suggestions to make the bottle like a piece of art. Please refer to Harlow whisky, Kelpa Rum, PLR and Vireo coffee for the inspiration and styles we like. For the words 1746 and Oat Whisky please make original fonts or artwork. We would like it to be in Serif font but we are open to suggestions
The bottle is as attached with the following dimensions
Height :159mm
Diammeter:84mm
Outter Diameter of mouth:39mm

We develop the world's first soy wines and spirits. Our new product is a soy based whisky that pays tribute to tradition and culture in Singapore while showcasing our nation's innovative and courageous spirit, moving from a swamp to a first world nation.

Please read the brand guidelines for deeper understanding

Target Market(s)

Global travellers coming to Singapore. Adventurous, innovators and independent self made pride.

Industry/Entity Type

Alcohol beverages

Requirements
Must have
• Original label design a box/packaging design, logo of morvane, logo of 1746, fonts and art of the labels
Nice to have
• Original artwork for 1746 and Oat Whisky. Batik prints, gold, soy beans/flowers, Singapore elements.
Should not have
• No copied work.

```html
<!DOCTYPE html>
<html lang="en">
<head>
<meta charset="utf-8">
<title>Morvane 1746 Oat Whisky – Label</title>
<link rel="stylesheet" href="https://fonts.googleapis.com/css2?family=Abril+Fatface&family=Oswald:wght@300;400&display=swap">
<style>
  :root {
    --stage: #1d2230;
    --label-green: #1c4a38;
    --medallion-green: #1f4d3a;
    --gold: #e0a73a;
    --gold-soft: #c9953a;
    --navy: #1f2440;
    --teal: #1f8a6e;
  }
  * { margin: 0; padding: 0; box-sizing: border-box; }
  html, body {
    width: 1200px; height: 1200px; overflow: hidden;
    background: var(--stage);
  }
  .label {
    position: absolute; left: 255px; top: 60px;
    width: 690px; height: 1080px;
    background: var(--label-green);
    border: 3px solid var(--gold-soft);
  }
  .label__inner-frame {
    position: absolute; inset: 12px;
    border: 2px solid var(--gold-soft);
  }
  .label__pattern {
    position: absolute; left: 22px; right: 22px; top: 22px; bottom: 110px;
    background:
      radial-gradient(circle at 20% 20%, rgba(224,167,58,.75), transparent 28%),
      radial-gradient(circle at 80% 25%, rgba(224,167,58,.65), transparent 26%),
      radial-gradient(circle at 15% 75%, rgba(224,167,58,.6), transparent 25%),
      radial-gradient(circle at 85% 80%, rgba(224,167,58,.6), transparent 25%),
      linear-gradient(160deg, var(--navy), var(--teal) 55%, var(--navy));
  }
  .brand {
    position: absolute; left: 0; right: 0; top: 150px;
    display: flex; flex-direction: column; align-items: center; gap: 14px;
  }
  .brand__mark {
    width: 92px; height: 92px; border-radius: 50%;
    background: var(--medallion-green);
    border: 3px solid var(--gold);
  }
  .brand__name {
    font-family: "Oswald", sans-serif; font-weight: 400;
    font-size: 34px; letter-spacing: 12px; color: var(--gold);
    background: var(--medallion-green); padding: 2px 10px 2px 22px;
  }
  .medallion {
    position: absolute; left: 50%; top: 616px;
    width: 520px; height: 520px; margin: -260px 0 0 -260px;
    border-radius: 50%;
    background: var(--medallion-green);
    border: 4px solid var(--gold-soft);
    box-shadow: 0 0 0 10px var(--medallion-green), 0 0 0 13px var(--gold-soft);
    display: flex; flex-direction: column; align-items: center; justify-content: center;
  }
  .medallion__year {
    font-family: "Abril Fatface", serif; color: var(--gold);
    font-size: 190px; line-height: 1; letter-spacing: -4px;
    transform: scaleX(.82); margin-top: 10px;
  }
  .medallion__kind {
    font-family: "Abril Fatface", serif; color: var(--gold);
    font-size: 70px; line-height: 1; transform: scaleX(.8); margin-top: 8px;
  }
  .details {
    position: absolute; left: 22px; right: 22px; bottom: 22px; height: 80px;
    display: flex; align-items: center; justify-content: space-between;
    padding: 0 26px;
    font-family: "Oswald", sans-serif; font-weight: 300; color: var(--gold);
  }
  .details__item { font-size: 26px; }
  .details__numbers { font-size: 17px; line-height: 1.5; }
</style>
</head>
<body>
  <main class="label">
    <div class="label__inner-frame"></div>
    <div class="label__pattern" role="img" aria-label="Gold and teal batik pattern of soy beans, leaves and flowers on navy"></div>

    <div class="brand">
      <div class="brand__mark"></div>
      <div class="brand__name">MORVANE</div>
    </div>

    <div class="medallion">
      <div class="medallion__year">1746</div>
      <div class="medallion__kind">Oat Whisky</div>
    </div>

    <div class="details">
      <span class="details__item">500ml</span>
      <span class="details__item">% ABV</span>
      <span class="details__item">Made in Singapore</span>
      <span class="details__numbers">Batch No:<br>Bottle No:</span>
    </div>
  </main>
</body>
</html>
```